Road Construction Company needs business cards

We would like a new business card designed for our business.

We're a road construction company based in Qld, Australia.

Can the business card please have the following information on it.

Name: Brent Malvoy
Position: General Manager
Phone: 0471 592 304
Email: Brent.malvoy@quendix.com.au
Address: 87 Harrowgate Ave, Pindarra, QLD, 4000
Website: www.quendix.com.au

Visually we'd like the card to be professional and simple.

Attached is our logo.

Our website is www.quendix.com.au

Target Market(s)

Men aged 25-60

Contact Information for Business Card

As listed in project description

Font styles to use
Serif

Requirements
Must have
• Large logo on back of card

```html
<!DOCTYPE html>
<html lang="en">
<head>
<meta charset="utf-8">
<title>Quendix Business Card</title>
<link href="https://fonts.googleapis.com/css2?family=Poppins:wght@400;600;700&family=Open+Sans:wght@400&display=swap" rel="stylesheet">
<style>
  :root {
    --brand-blue: #0f57a3;
    --back-blue: #0f5aa6;
    --accent-blue: #2a9fdc;
    --label-grey: #555555;
    --page-bg: #ffffff;
    --card-white: #ffffff;
  }
  * { margin: 0; padding: 0; box-sizing: border-box; }
  html, body { width: 1200px; height: 1000px; overflow: hidden; background: var(--page-bg); }
  .canvas { position: relative; width: 1200px; height: 1000px; }

  .side-label {
    position: absolute;
    font-family: "Open Sans", sans-serif;
    font-size: 22px;
    color: var(--label-grey);
  }
  .side-label--front { left: 396px; top: 318px; }
  .side-label--back { left: 808px; top: 70px; }

  .card {
    position: absolute;
    width: 294px;
    height: 530px;
    box-shadow: 4px 8px 14px rgba(0,0,0,0.22);
    font-family: "Poppins", sans-serif;
    text-align: center;
  }
  .card--front { left: 86px; top: 323px; background: var(--card-white); color: var(--brand-blue); }
  .card--back { left: 495px; top: 75px; background: var(--back-blue); color: #ffffff; }

  .brand-name { position: absolute; left: 0; right: 0; font-weight: 700; }
  .card--front .brand-name { top: 58px; font-size: 22px; letter-spacing: 0.5px; color: var(--brand-blue); }
  .card--back .brand-name { top: 272px; font-size: 50px; letter-spacing: 1px; color: #ffffff; }

  .holder-name { position: absolute; left: 0; right: 0; top: 190px; font-size: 28px; font-weight: 600; }
  .holder-role { position: absolute; left: 0; right: 0; top: 235px; font-size: 16px; color: var(--accent-blue); }
  .holder-role .chev { font-size: 12px; position: relative; top: -1px; margin: 0 6px; }

  .contact-list { position: absolute; left: 0; right: 0; top: 324px; list-style: none; }
  .contact-item { display: flex; flex-direction: column; align-items: center; }
  .contact-item svg { fill: var(--brand-blue); display: block; }
  .contact-item--phone svg { width: 20px; height: 20px; }
  .contact-item--email { margin-top: 8px; }
  .contact-item--email svg { width: 22px; height: 16px; }
  .contact-item--address { margin-top: 14px; }
  .contact-item--address svg { width: 18px; height: 22px; }
  .contact-text { font-size: 13px; margin-top: 4px; }
  .contact-item--address .contact-text { font-size: 10.5px; margin-top: 8px; }

  .web-address { position: absolute; left: 0; right: 0; top: 472px; font-size: 21px; }
</style>
</head>
<body>
<main class="canvas">
  <span class="side-label side-label--front">Front</span>
  <span class="side-label side-label--back">Back</span>

  <section class="card card--front">
    <div class="brand-name">QUENDIX</div>
    <h1 class="holder-name">Brent Malvoy</h1>
    <p class="holder-role"><span class="chev">&#9664;</span>General Manager<span class="chev">&#9654;</span></p>
    <ul class="contact-list">
      <li class="contact-item contact-item--phone">
        <svg viewBox="0 0 24 24" aria-hidden="true"><path d="M6.6 10.8c1.4 2.8 3.8 5.1 6.6 6.6l2.2-2.2c.3-.3.7-.4 1-.2 1.1.4 2.3.6 3.6.6.6 0 1 .4 1 1V20c0 .6-.4 1-1 1C10.6 21 3 13.4 3 4c0-.6.4-1 1-1h3.5c.6 0 1 .4 1 1 0 1.3.2 2.5.6 3.6.1.3 0 .7-.2 1l-2.3 2.2z"/></svg>
        <span class="contact-text">0471 592 304</span>
      </li>
      <li class="contact-item contact-item--email">
        <svg viewBox="0 0 22 16" aria-hidden="true"><path d="M0 0h22v2.2L11 9 0 2.2z"/><path d="M0 4.6l11 6.8 11-6.8V16H0z"/></svg>
        <span class="contact-text">brent.malvoy@quendix.com.au</span>
      </li>
      <li class="contact-item contact-item--address">
        <svg viewBox="0 0 18 22" aria-hidden="true"><path d="M9 0C4 0 0 4 0 9c0 6.5 9 13 9 13s9-6.5 9-13c0-5-4-9-9-9zm0 12.5a3.5 3.5 0 110-7 3.5 3.5 0 010 7z"/></svg>
        <span class="contact-text">87 Harrowgate Ave, Pindarra, QLD, 4000</span>
      </li>
    </ul>
  </section>

  <section class="card card--back">
    <div class="brand-name">QUENDIX</div>
    <p class="web-address">www.quendix.com.au</p>
  </section>
</main>
</body>
</html>
```